Delivery Performance Dashboard for Web Portal

We need you to design a dashboard for our web portal. We deliver sand and stone to construction jobsites. The attached screenshot is from our current web portal dashboard . It shows how much material has been delivered from an order.

Dump trucks will deliver multiple loads during the day and the dispatcher uses the dashboard to monitor if they need to add more trucks or less trucks to fulfill the order. An example would be, I need to ship 1,000 tons of sand to a jobsite and I plan to use 10 trucks during the day and that it will take 10 hours of hauling to complete the job. After 5 hours of hauling (50% the day is over), I should have delivered 500 tons of sand (50% of the order). But maybe there is a lot of traffic, and I only have delivered 300 tons. The dashboard will show that I am behind schedule and I might need to add 2 more trucks to the job.

Industry/Entity Type

Construction

Font styles to use
Sans Serif

Requirements
Must have
• We need a progress bar showing how much material has been delivered, how much material was requested to be delivered total and how much material should have been delivered at the current time. The goal is to show the user if the deliveries are ahead or behind the expected pace and why.
Nice to have
• The icons for plant, driving and jobsite show if the actual times have exceeded or beaten the planned times. Maybe you have other ideas to show the user if the trucks are sitting longer on the jobsite, at the plant to get loaded or driving to and from the jobsite.

```html
<!DOCTYPE html>
<html lang="en">
<head>
<meta charset="utf-8">
<title>Delivery Performance Dashboard</title>
<link href="https://fonts.googleapis.com/css2?family=Roboto:wght@400;500;700&display=swap" rel="stylesheet">
<style>
:root{
  --cyan:#00c3ea;
  --cyan-soft:#d6f5fc;
  --ink:#111418;
  --muted:#8a8f96;
  --field:#eef2f6;
  --page:#f8fafc;
  --white:#ffffff;
  --alert:#ff0000;
  --ok:#2ecc71;
  --track:#eef2f6;
  --rule:#9aa0a6;
}
*{box-sizing:border-box;margin:0;padding:0}
html,body{width:1200px;height:675px;overflow:hidden}
body{font-family:"Roboto",sans-serif;color:var(--ink);background:var(--page);position:relative}
.abs{position:absolute}
.topbar{left:0;top:0;width:1200px;height:76px;background:var(--white);border-bottom:1px solid var(--rule)}
.brand{left:73px;top:32px;font-size:13px;font-weight:700;letter-spacing:.1px}
.top-search{left:808px;top:32px;display:flex;align-items:center;gap:8px;font-size:12px}
.bell{left:926px;top:33px}
.avatar{border-radius:50%;background:linear-gradient(160deg,#c9c4bf,#7d746c)}
.user-avatar{left:980px;top:24px;width:33px;height:33px}
.user-name{left:1028px;top:32px;font-size:13px;font-weight:500}
.filters{left:0;top:77px;width:1200px;height:74px;background:var(--white)}
.field{background:var(--field);height:28px;top:101px;display:flex;align-items:center;justify-content:space-between;padding:0 10px;font-size:12px;color:var(--muted)}
.label{top:108px;font-size:11.5px;font-weight:700}
.order-list{left:73px;top:195px;width:290px}
.order-item{height:73px;margin-bottom:7px;background:var(--white);display:flex;align-items:center;padding-left:20px;gap:17px}
.order-item .avatar{width:40px;height:40px;flex:none}
.order-item h3{font-size:15.5px;font-weight:500;line-height:1.1}
.order-item p{font-size:12.5px;font-weight:500;color:var(--muted);margin-top:2px}
.order-item.active{background:var(--cyan);color:var(--white)}
.order-item.active p{color:var(--white)}
.scroll-thumb{left:372px;top:195px;width:5px;height:73px;border-radius:3px;background:var(--cyan)}
.detail-card{left:372px;top:198px;width:755px;height:430px;background:var(--white)}
.divider{left:743px;top:198px;width:1px;height:430px;background:var(--field)}
.center{transform:translateX(-50%);text-align:center}
.truck-art{left:429px;top:244px;width:105px;height:70px;border-radius:6px;background:linear-gradient(135deg,var(--cyan-soft),#9fe6f6)}
.alert-text{top:243px;left:647px;color:var(--alert);font-size:12.5px;font-weight:500;line-height:16px;width:112px}
.bar{height:14px;border-radius:7px;background:var(--track)}
.bar i{display:block;height:100%;border-radius:7px}
.pace-bar{left:573px;top:279px;width:148px}
.pace-bar i{width:92%;background:var(--alert)}
.advice{top:300px;left:641px;color:var(--ok);font-size:12.5px;font-weight:500;white-space:nowrap}
.fact h4{font-size:13px;font-weight:500}
.fact p{font-size:11.5px;font-weight:500;color:var(--muted);line-height:15px;margin-top:3px}
.fact svg{display:block;margin:0 auto 10px}
.stat{top:262px;width:110px}
.stat h4{font-size:13px;font-weight:500;line-height:17px;margin-top:8px}
.stat-bar{display:flex;align-items:center;gap:7px;margin-top:10px;font-size:10px;padding-left:14px}
.stat-bar .bar{width:60px;height:6px}
.stat-bar .bar i{background:var(--cyan)}
.totals{left:789px;top:438px;width:292px}
.totals div{display:flex;justify-content:space-between;height:44px;font-size:13px}
.totals span:first-child{color:var(--muted);font-weight:500}
.totals span:last-child{font-weight:500}
</style>
</head>
<body>
<header class="abs topbar"></header>
<div class="abs brand">COMPANY NAME</div>
<div class="abs top-search">
  <svg width="16" height="16" viewBox="0 0 16 16" fill="none" stroke="#111" stroke-width="1.8"><circle cx="7" cy="7" r="5.5"/><path d="M11 11l4 4"/></svg>Search
</div>
<svg class="abs bell" width="14" height="17" viewBox="0 0 14 17" fill="none" stroke="#111" stroke-width="1.2"><path d="M2 12V7a5 5 0 0110 0v5l1.5 1.5h-13z"/><path d="M5.5 15a1.5 1.5 0 003 0"/></svg>
<div class="abs avatar user-avatar" role="img" aria-label="Dispatcher profile photo"></div>
<div class="abs user-name">Dispatcher A</div>

<section class="abs filters"></section>
<div class="abs field" style="left:73px;width:216px">Search order
  <svg width="15" height="15" viewBox="0 0 16 16" fill="none" stroke="#666" stroke-width="1.4"><circle cx="7" cy="7" r="5.5"/><path d="M11 11l4 4"/></svg></div>
<div class="abs label" style="left:359px">Status</div>
<div class="abs field" style="left:403px;width:83px;color:#666">Active
  <svg width="10" height="6" viewBox="0 0 10 6" fill="none" stroke="#666" stroke-width="1.3"><path d="M1 1l4 4 4-4"/></svg></div>
<div class="abs label" style="left:569px">Location</div>
<div class="abs field" style="left:626px;width:105px">New York
  <svg width="10" height="6" viewBox="0 0 10 6" fill="none" stroke="#666" stroke-width="1.3"><path d="M1 1l4 4 4-4"/></svg></div>
<div class="abs label" style="left:794px">Date</div>
<div class="abs field" style="left:832px;width:111px">1 Jul 2020
  <svg width="13" height="13" viewBox="0 0 13 13" fill="#888"><rect x="0" y="1" width="13" height="12" rx="1"/><rect x="1.5" y="4" width="10" height="7.5" fill="#eef2f6"/><rect x="3" y="5.5" width="2" height="2"/><rect x="6" y="5.5" width="2" height="2"/><rect x="9" y="5.5" width="1.5" height="2"/><rect x="3" y="8.5" width="2" height="2"/><rect x="6" y="8.5" width="2" height="2"/></svg></div>
<div class="abs" style="left:950px;top:107px;font-size:12px">-</div>
<div class="abs field" style="left:962px;width:111px">2 Jul 2020
  <svg width="13" height="13" viewBox="0 0 13 13" fill="#888"><rect x="0" y="1" width="13" height="12" rx="1"/><rect x="1.5" y="4" width="10" height="7.5" fill="#eef2f6"/><rect x="3" y="5.5" width="2" height="2"/><rect x="6" y="5.5" width="2" height="2"/><rect x="9" y="5.5" width="1.5" height="2"/><rect x="3" y="8.5" width="2" height="2"/><rect x="6" y="8.5" width="2" height="2"/></svg></div>

<nav class="abs order-list">
  <div class="order-item"><div class="avatar" role="img" aria-label="Customer contact photo"></div><div><h3>Halden Construction</h3><p>North Division</p></div></div>
  <div class="order-item active"><div class="avatar" role="img" aria-label="Customer contact photo"></div><div><h3>Halden Construction</h3><p>North Division</p></div></div>
  <div class="order-item"><div class="avatar" role="img" aria-label="Customer contact photo"></div><div><h3>Halden Construction</h3><p>North Division</p></div></div>
  <div class="order-item"><div class="avatar" role="img" aria-label="Customer contact photo"></div><div><h3>Halden Construction</h3><p>North Division</p></div></div>
  <div class="order-item"><div class="avatar" role="img" aria-label="Customer contact photo"></div><div><h3>Halden Construction</h3><p>North Division</p></div></div>
  <div class="order-item"><div class="avatar" role="img" aria-label="Customer contact photo"></div><div><h3>Halden Construction</h3><p>North Division</p></div></div>
</nav>

<main class="abs detail-card"></main>
<div class="abs scroll-thumb"></div>
<div class="abs divider"></div>

<div class="abs truck-art" role="img" aria-label="Illustration of a loaded dump truck"></div>
<div class="abs center alert-text">Oops! Running behind Schedule</div>
<div class="abs bar pace-bar"><i></i></div>
<div class="abs center advice">Add 2 More Trucks</div>

<div class="abs center fact" style="left:490px;top:370px">
  <svg width="28" height="24" viewBox="0 0 28 24" fill="none" stroke="var(--cyan)" stroke-width="1.5"><rect x="2" y="10" width="13" height="10"/><path d="M15 13h6l4 4v3H15"/><circle cx="6" cy="21" r="2"/><circle cx="21" cy="21" r="2"/><path d="M12 2h8v8"/></svg>
  <h4>Order</h4><p>#17746</p></div>
<div class="abs center fact" style="left:625px;top:366px">
  <svg width="32" height="22" viewBox="0 0 32 22" fill="none" stroke="var(--cyan)" stroke-width="1.5"><path d="M2 6h18v10H2z"/><path d="M20 8h6l4 4v4H20"/><circle cx="7" cy="18" r="2"/><circle cx="14" cy="18" r="2"/><circle cx="25" cy="18" r="2"/><path d="M6 6v10M11 6v10M16 6v10"/></svg>
  <h4>Origin</h4><p>Brightwater<br>Asphalt Plant</p></div>
<div class="abs center fact" style="left:490px;top:488px">
  <svg width="28" height="24" viewBox="0 0 28 24" fill="none" stroke="var(--cyan)" stroke-width="1.5"><path d="M12 4l12-2 2 10-12 4z"/><path d="M2 12h8v8H2z"/><path d="M10 16h16v4H10"/><circle cx="6" cy="21" r="2"/><circle cx="20" cy="21" r="2"/></svg>
  <h4>Destination</h4><p>BZJV - 185<br>from mm<br>77 - 98</p></div>
<div class="abs center fact" style="left:625px;top:507px">
  <svg width="22" height="22" viewBox="0 0 22 22"><circle cx="11" cy="11" r="11" fill="var(--ok)"/><path d="M6 11l3.5 3.5L16 8" fill="none" stroke="#fff" stroke-width="2.2"/></svg>
  <h4>Status</h4><p>Accepted</p></div>

<div class="abs center stat" style="left:813px">
  <svg width="32" height="28" viewBox="0 0 32 28" fill="none" stroke="var(--cyan)" stroke-width="1.5"><path d="M12 6l14-4 3 12-14 4z"/><path d="M2 14h9v8H2z"/><path d="M11 18h18v4H11"/><circle cx="6" cy="24" r="2"/><circle cx="22" cy="24" r="2"/></svg>
  <h4>300 Tons<br>Delivered</h4>
  <div class="stat-bar"><div class="bar"><i style="width:74%"></i></div>40%</div></div>
<div class="abs center stat" style="left:936px">
  <svg width="36" height="28" viewBox="0 0 36 28" fill="none" stroke="var(--cyan)" stroke-width="1.5"><path d="M14 6h20v14H14z"/><path d="M14 10H7l-5 6v6h32"/><circle cx="8" cy="23" r="2.5"/><circle cx="24" cy="23" r="2.5"/><circle cx="30" cy="23" r="2.5"/><path d="M19 6v14M24 6v14M29 6v14"/></svg>
  <h4>3 Trucks<br>Used</h4>
  <div class="stat-bar"><div class="bar"><i style="width:74%"></i></div>35%</div></div>
<div class="abs center stat" style="left:1058px">
  <svg width="28" height="28" viewBox="0 0 28 28" fill="none" stroke="var(--cyan)" stroke-width="1.5"><rect x="2" y="4" width="22" height="20" rx="2"/><path d="M2 10h22M7 2v4M19 2v4"/><circle cx="21" cy="21" r="5" fill="#fff"/><path d="M21 18v3h2"/></svg>
  <h4>Time<br>Spent</h4>
  <div class="stat-bar"><div class="bar"><i style="width:60%"></i></div>35%</div></div>

<div class="abs totals">
  <div><span>Total Tonnage Order</span><span>1,000 Tons</span></div>
  <div><span>Total No. of Trucks</span><span>10 Trucks</span></div>
  <div><span>Time</span><span>10 Hours</span></div>
</div>
</body>
</html>
```